HLT Crown Business Card Design 2020

Our Manor Steward is looking for a business card that is clean and straight to the point but still looks high-end and attractive. We are a team comprised of management and field professionals focused on the high-end residential marketplace. We serve homeowners and trade professionals directly based out of the Metrowest/Boston area. We provide client services as well as construction/renovation services.
We are aiming for a black and white feel (white background and black text) and a matte finish with rounded edges.

We want to emphasis our vision of "Properties - Projects - Partners".
Dana Fellmore is the president of HLT

Please include the following areas we service: Boston/Cape/Newport
Please make sure to include Dana's mobile (555) 302 4187 & office number (555) 640 2913, email dana@ourmanorsteward.example and website www.ourmanorsteward.example

Colors

Designer to choose only greyscale colors for use in the design.

Requirements
Must have
• Include "Properties - Projects - Partners" in design

Include "After Hours Emergency Support # 1800 555 0142" with icon

```html
<!DOCTYPE html>
<html lang="en">
<head>
<meta charset="utf-8">
<title>HLT Crown Business Card</title>
<link rel="stylesheet" href="https://fonts.googleapis.com/css2?family=Montserrat:wght@600;700&family=Open+Sans:wght@400;600&display=swap">
<style>
  :root {
    --backdrop: #e4e4e4;
    --ink: #1b1b1b;
    --paper: #ffffff;
    --muted: #3a3a3a;
    --soft: #bdbdbd;
    --card-shadow: rgba(0, 0, 0, 0.18);
  }
  * { box-sizing: border-box; margin: 0; padding: 0; }
  html, body { width: 1200px; height: 800px; overflow: hidden; }
  body {
    background: var(--backdrop);
    display: flex;
    align-items: center;
    justify-content: center;
    gap: 48px;
    font-family: "Open Sans", Arial, sans-serif;
  }
  .card {
    width: 520px;
    height: 300px;
    border-radius: 14px;
    box-shadow: 0 10px 28px var(--card-shadow);
    position: relative;
    overflow: hidden;
  }
  /* Front */
  .card--front {
    background: var(--ink);
    color: var(--paper);
    display: flex;
    flex-direction: column;
    align-items: center;
    justify-content: center;
    padding-bottom: 30px;
  }
  .brand { display: flex; flex-direction: column; align-items: center; }
  .brand__mark {
    font-family: "Montserrat", Arial, sans-serif;
    font-weight: 700;
    font-size: 78px;
    line-height: 1;
    letter-spacing: -1px;
  }
  .brand__name {
    font-family: "Montserrat", Arial, sans-serif;
    font-weight: 700;
    font-size: 15px;
    letter-spacing: 3px;
    text-transform: uppercase;
    margin-top: 10px;
  }
  .tagline {
    font-family: "Open Sans", Arial, sans-serif;
    font-weight: 400;
    font-size: 11px;
    letter-spacing: 2px;
    text-transform: uppercase;
    color: var(--soft);
    margin-top: 10px;
  }
  .service-areas {
    position: absolute;
    bottom: 30px;
    left: 0; right: 0;
    text-align: center;
    font-size: 12px;
    letter-spacing: 0.4px;
  }
  .service-areas .dot { margin: 0 6px; }
  /* Back */
  .card--back {
    background: var(--paper);
    color: var(--ink);
  }
  .card--back .brand {
    position: absolute;
    top: 38px;
    right: 52px;
  }
  .card--back .brand__mark { font-size: 58px; color: var(--ink); }
  .card--back .brand__name { font-size: 11px; letter-spacing: 2px; margin-top: 6px; }
  .person {
    position: absolute;
    left: 44px;
    bottom: 98px;
  }
  .person__name {
    font-weight: 600;
    font-size: 16px;
    text-transform: uppercase;
  }
  .person__title { font-size: 12px; color: var(--muted); margin-top: 1px; }
  .contacts {
    position: absolute;
    left: 44px;
    bottom: 24px;
    display: grid;
    grid-template-columns: auto auto;
    column-gap: 18px;
    row-gap: 4px;
    font-size: 12px;
    color: var(--muted);
  }
  .contact { display: flex; align-items: center; gap: 6px; white-space: nowrap; }
  .contact svg { width: 12px; height: 12px; fill: var(--ink); flex: none; }
  .contact--emergency {
    grid-column: 1 / -1;
    margin-top: 4px;
    color: var(--ink);
    font-weight: 600;
  }
</style>
</head>
<body>
  <section class="card card--front" aria-label="Business card front">
    <div class="brand">
      <span class="brand__mark">HLT</span>
      <span class="brand__name">Our Manor Steward</span>
      <span class="tagline">Properties - Projects - Partners</span>
    </div>
    <p class="service-areas">
      <span class="dot">&#9679;</span>Boston<span class="dot">&#9679;</span>Metrowest<span class="dot">&#9679;</span>South Shore<span class="dot">&#9679;</span>Cape<span class="dot">&#9679;</span>Newport
    </p>
  </section>

  <section class="card card--back" aria-label="Business card back">
    <div class="brand">
      <span class="brand__mark">HLT</span>
      <span class="brand__name">Our Manor Steward</span>
    </div>
    <div class="person">
      <p class="person__name">Dana Fellmore</p>
      <p class="person__title">President</p>
    </div>
    <div class="contacts">
      <span class="contact">
        <svg viewBox="0 0 12 12" aria-hidden="true"><path d="M3 0h6a1 1 0 0 1 1 1v10a1 1 0 0 1-1 1H3a1 1 0 0 1-1-1V1a1 1 0 0 1 1-1zm0 1.5v8h6v-8zM6 10.2a.6.6 0 1 0 0 1.2.6.6 0 0 0 0-1.2z"/></svg>
        (555) 302 4187
      </span>
      <span class="contact">
        <svg viewBox="0 0 12 12" aria-hidden="true"><path d="M0 2h12v8H0zm1 1v.4l5 3.2 5-3.2V3zm0 1.6V9h10V4.6L6 7.8z"/></svg>
        dana@ourmanorsteward.example
      </span>
      <span class="contact">
        <svg viewBox="0 0 12 12" aria-hidden="true"><path d="M1 3c0-1 1-2 5-2s5 1 5 2v1H8.5V3h-5v1H1zm2 2h6l2 3v3H1V8zm3 1.2a1.3 1.3 0 1 0 0 2.6 1.3 1.3 0 0 0 0-2.6z"/></svg>
        (555) 640 2913
      </span>
      <span class="contact">
        <svg viewBox="0 0 12 12" aria-hidden="true"><path d="M6 0a6 6 0 1 0 0 12A6 6 0 0 0 6 0zm0 1c.7 0 1.5 1.6 1.7 4.5H4.3C4.5 2.6 5.3 1 6 1zM1 6.5h2.3c.1 1.5.4 2.8.8 3.6A5 5 0 0 1 1 6.5zm0-1A5 5 0 0 1 4.1 1.9c-.4.8-.7 2.1-.8 3.6zm5 5.5c-.7 0-1.5-1.6-1.7-4.5h3.4C7.5 9.4 6.7 11 6 11zm1.9-.9c.4-.8.7-2.1.8-3.6H11a5 5 0 0 1-3.1 3.6zM8.7 5.5c-.1-1.5-.4-2.8-.8-3.6A5 5 0 0 1 11 5.5z"/></svg>
        www.ourmanorsteward.example
      </span>
      <span class="contact contact--emergency">
        <svg viewBox="0 0 12 12" aria-hidden="true"><path d="M6 .5 11.8 11H.2zM5.3 4v3.8h1.4V4zm0 4.8v1.3h1.4V8.8z"/></svg>
        After Hours Emergency Support # 1800 555 0142
      </span>
    </div>
  </section>
</body>
</html>
```